New Human Resources Outsourcing company needs a brochure to explain services

I need a brochure that describes my business and the services we offer.

Everything we do is on my website as well. www.kelvorastaffing.com

Target Market(s)

Business Owners (Manufacturing, I.T. Financial Services)

Industry/Entity Type

Business

```html
<!DOCTYPE html>
<html lang="en">
<head>
<meta charset="UTF-8">
<title>Kelvora Staffing – Service Levels Brochure</title>
<link rel="stylesheet" href="https://fonts.googleapis.com/css2?family=Cabin:ital,wght@0,400;0,600;1,600&display=swap">
<style>
  :root {
    --backdrop: #e4e4e6;
    --purple: #704c9c;
    --purple-deep: #5e3f88;
    --teal: #27ab9c;
    --teal-deep: #1f9487;
    --paper: #ffffff;
    --ink-grey: #5a5a5a;
    --ink-white: #ffffff;
    --lavender: #cfc4e0;
    --mint: #bfe4de;
  }
  * { box-sizing: border-box; margin: 0; padding: 0; }
  html, body {
    width: 1200px; height: 800px; overflow: hidden;
    background: var(--backdrop);
    font-family: "Cabin", sans-serif;
  }
  .brochure {
    position: absolute; left: 60px; top: 50px;
    width: 1080px; height: 700px;
    display: flex;
    box-shadow: 0 10px 30px rgba(0,0,0,0.15);
  }
  .panel {
    position: relative; width: 360px; height: 700px; overflow: hidden;
  }
  .panel + .panel { border-left: 1px solid rgba(0,0,0,0.06); }
  .panel--premier { background: var(--purple); color: var(--ink-white); }
  .panel--elite { background: var(--paper); color: var(--ink-grey); }
  .panel--deluxe { background: var(--teal); color: var(--ink-white); }

  .panel__photo {
    position: absolute; left: 0; top: 0; width: 100%; height: 270px;
    clip-path: polygon(0 0, 100% 0, 100% 82%, 50% 100%, 0 82%);
  }
  .photo--handshake { background: linear-gradient(160deg, #eef1f4 0%, #b9c4d0 45%, #4a5568 100%); }
  .photo--hr-interface { background: linear-gradient(150deg, #4b5563 0%, #2a3038 45%, #8c97a6 100%); }
  .photo--keyboard { background: linear-gradient(170deg, #eceaf0 0%, #d9d2d6 40%, #b08e6a 75%, #8a6a4b 100%); }

  .panel__pattern {
    position: absolute; left: 0; bottom: 0; width: 100%; height: 300px;
  }
  .panel--premier .panel__pattern { background: linear-gradient(200deg, transparent 30%, rgba(255,255,255,0.10) 70%, rgba(94,63,136,0.6) 100%); }
  .panel--elite .panel__pattern { background: linear-gradient(200deg, var(--mint) 0%, #f2f2f4 45%, var(--lavender) 100%); opacity: 0.7; }
  .panel--deluxe .panel__pattern { background: linear-gradient(200deg, rgba(255,255,255,0.10) 0%, transparent 40%, var(--teal-deep) 100%); }

  .panel__body {
    position: absolute; left: 40px; right: 36px; top: 300px;
  }
  .panel__title {
    font-size: 30px; font-weight: 600; margin-bottom: 10px; letter-spacing: 0.2px;
  }
  .panel--premier .panel__title { font-style: italic; }
  .panel--elite .panel__title { color: #4d4d4d; }
  .panel__text { font-size: 15px; line-height: 1.45; }
</style>
</head>
<body>
  <main class="brochure">
    <section class="panel panel--premier">
      <div class="panel__photo photo--handshake" role="img" aria-label="Photo of business people shaking hands in a bright office"></div>
      <div class="panel__pattern" role="img" aria-label="Faint decorative cube grid pattern"></div>
      <div class="panel__body">
        <h2 class="panel__title">Premier</h2>
        <p class="panel__text">This is our highest level of service providing your company's complete HR Department. We will handle Benefit Administration, Employee Relations and other HR functions. Your HR professional will come on site two days per week to handle all HR duties, meet with employees and partner with Management on strategic planning and organization development.</p>
      </div>
    </section>

    <section class="panel panel--elite">
      <div class="panel__photo photo--hr-interface" role="img" aria-label="Photo of a businessman touching a digital HR hexagon interface with people and chart icons"></div>
      <div class="panel__pattern" role="img" aria-label="Decorative cube grid pattern in mint and lavender"></div>
      <div class="panel__body">
        <h2 class="panel__title">Elite</h2>
        <p class="panel__text">With this level of service your HR professional will come on site one day per week to handle all HR duties with most tasks being completed off-site. We will provide you with the tools and off-site support necessary to run an effective HR Department.</p>
      </div>
    </section>

    <section class="panel panel--deluxe">
      <div class="panel__photo photo--keyboard" role="img" aria-label="Photo of hands using a computer mouse and keyboard on a wooden desk"></div>
      <div class="panel__pattern" role="img" aria-label="Faint decorative cube grid pattern"></div>
      <div class="panel__body">
        <h2 class="panel__title">Deluxe</h2>
        <p class="panel__text">With this level of service your HR professional will come on site once per month and provide virtual HR support with most tasks and support being provided off-site. This level of service is ideal for companies who do not require an on-site presence and just need a back office and trusted partner to ensure they remain compliant.</p>
      </div>
    </section>
  </main>
</body>
</html>
```